Social Media Infographic for White Paper

Am working on a white paper on social media use by C-Suite Executives, and hope to include some infographics. I would like some help designing the first infographic.

The master bit of information is that "66% of C-Suite Executives use social media for professional purpose."

Within that 66%
-70% post original content on a daily/weekly basis
-13% of professional users are lurkers
-40% plan to use social media even more in the future

After initial design will need to two versions of the infographic, one listing the source at the bottom in small print (Source: 2017 Venmoor Partners Executive Social Media Study), the other one with no source information.

Infographic design should be complimentary with my website: www.venmoorpartners.example, but use of green should be very limited, if at all.

Target Market(s)

New media, C-Suite Executives, Executive Coaches

Industry/Entity Type

Management Consulting

Font styles to use
Sans Serif

Requirements
Must have
• Infographic with data displayed in a easy to understand format that tells the story of C-Suite Executives that participate in social media for professional purposes.
Nice to have
• Complements website design - www.venmoor.example.
Should not have
• Limit use of green from website logo, which can be overpowering. Some is ok, but not too much

```html
<!DOCTYPE html>
<html lang="en">
<head>
<meta charset="utf-8">
<title>C-Suite Executives on Social Media</title>
<link rel="stylesheet" href="https://fonts.googleapis.com/css2?family=Oswald:wght@500&family=Montserrat:wght@500&display=swap">
<style>
  :root {
    --green: #5e9732;
    --ink: #2a2c28;
    --muted: #8a8785;
    --panel: #d9d9d9;
    --paper: #ffffff;
    --text: #2b2b2b;
  }
  html, body { margin: 0; padding: 0; overflow: hidden; background: var(--paper); }
  .canvas {
    position: relative; width: 1200px; height: 846px; box-sizing: border-box;
    border: 1px solid var(--ink); background: var(--paper); overflow: hidden;
    font-family: "Montserrat", Arial, sans-serif; color: var(--text);
  }
  .stat {
    position: absolute; left: 312px; margin: 0;
    font-family: "Oswald", "Arial Narrow", sans-serif; font-weight: 500;
    color: var(--green); font-size: 78px; line-height: 1; letter-spacing: -1px;
  }
  .caption {
    position: absolute; margin: 0; font-size: 25px; line-height: 32px;
    font-weight: 500; letter-spacing: 0.3px;
  }
  .figure-row { position: absolute; display: flex; }
  .figure { display: block; border-radius: 38% 38% 10% 10% / 45% 45% 8% 8%; }
  .figure.is-active { background: var(--ink); }
  .figure.is-idle { background: var(--muted); }
  .figure-row--lead { left: 22px; top: 94px; gap: 13px; }
  .figure-row--lead .figure { width: 104px; height: 110px; }
  .figure-row--sub .figure { width: 64px; height: 68px; }
  .figure-row--sub { left: 244px; gap: 9.6px; }
  .breakdown {
    position: absolute; left: 228px; top: 198px; width: 758px; height: 576px;
    box-sizing: border-box; background: var(--panel); border: 3px solid var(--ink);
  }
  .divider { position: absolute; left: 228px; width: 758px; height: 3px; background: var(--ink); }
  .source {
    position: absolute; left: 0; right: 0; top: 795px; margin: 0;
    text-align: center; font-size: 24px; font-weight: 500; letter-spacing: 0.4px;
  }
</style>
</head>
<body>
<main class="canvas">
  <p class="stat" style="top:14px">66%</p>
  <p class="caption" style="left:472px; top:16px">of C-Suite Executives use social<br>media for professional purpose</p>

  <div class="breakdown"></div>
  <div class="divider" style="top:226px"></div>
  <div class="divider" style="top:410px"></div>
  <div class="divider" style="top:590px"></div>

  <div class="figure-row figure-row--lead" role="img" aria-label="Ten executive pictograms at laptops, six highlighted">
    <span class="figure is-idle"></span><span class="figure is-idle"></span>
    <span class="figure is-active"></span><span class="figure is-active"></span>
    <span class="figure is-active"></span><span class="figure is-active"></span>
    <span class="figure is-active"></span><span class="figure is-active"></span>
    <span class="figure is-idle"></span><span class="figure is-idle"></span>
  </div>

  <p class="stat" style="top:244px">70%</p>
  <p class="caption" style="left:470px; top:244px">post original content on<br>a daily/weekly basis</p>
  <div class="figure-row figure-row--sub" style="top:324px" role="img" aria-label="Ten executive pictograms, seven highlighted">
    <span class="figure is-active"></span><span class="figure is-active"></span>
    <span class="figure is-active"></span><span class="figure is-active"></span>
    <span class="figure is-active"></span><span class="figure is-active"></span>
    <span class="figure is-active"></span><span class="figure is-idle"></span>
    <span class="figure is-idle"></span><span class="figure is-idle"></span>
  </div>

  <p class="stat" style="top:424px">13%</p>
  <p class="caption" style="left:474px; top:424px">of professional<br>users are lurkers</p>
  <div class="figure-row figure-row--sub" style="top:504px" role="img" aria-label="Ten executive pictograms, one highlighted">
    <span class="figure is-active"></span><span class="figure is-idle"></span>
    <span class="figure is-idle"></span><span class="figure is-idle"></span>
    <span class="figure is-idle"></span><span class="figure is-idle"></span>
    <span class="figure is-idle"></span><span class="figure is-idle"></span>
    <span class="figure is-idle"></span><span class="figure is-idle"></span>
  </div>

  <p class="stat" style="top:604px">40%</p>
  <p class="caption" style="left:472px; top:604px">plan to use social media<br>even more in the future</p>
  <div class="figure-row figure-row--sub" style="top:684px" role="img" aria-label="Ten executive pictograms, four highlighted">
    <span class="figure is-active"></span><span class="figure is-active"></span>
    <span class="figure is-active"></span><span class="figure is-active"></span>
    <span class="figure is-idle"></span><span class="figure is-idle"></span>
    <span class="figure is-idle"></span><span class="figure is-idle"></span>
    <span class="figure is-idle"></span><span class="figure is-idle"></span>
  </div>

  <p class="source">Source: 2017 Venmoor Partners Executive Social Media Study</p>
</main>
</body>
</html>
```